Oil and Gas Exploration and Production company needs a business card design

We need a business card design using our logo and colors in the logo. We want a mainstream design.

```html
<!DOCTYPE html>
<html lang="en">
<head>
<meta charset="utf-8">
<title>Vireo Oil &amp; Gas — Business Card</title>
<link rel="stylesheet" href="https://fonts.googleapis.com/css2?family=Merriweather:wght@400;700;900&display=swap">
<style>
  :root {
    --page-bg: #d9d4cc;
    --card-top: #eeeeec;
    --card-top-edge: #e2e2df;
    --band: #0b0b0c;
    --ink: #111111;
    --gold: #c28a2b;
    --white: #f4f4f2;
    --rule: #6b6b6b;
  }
  * { margin: 0; padding: 0; box-sizing: border-box; }
  html, body { width: 1200px; height: 970px; overflow: hidden; }
  body {
    background: var(--page-bg);
    font-family: "Merriweather", Georgia, serif;
    position: relative;
  }
  .card {
    position: absolute;
    left: 100px; top: 188px;
    width: 1000px; height: 593px;
    background: linear-gradient(180deg, var(--card-top) 0%, var(--card-top-edge) 100%);
    overflow: hidden;
    box-shadow: 0 10px 30px rgba(0,0,0,.18);
  }
  .brand {
    position: absolute;
    top: 122px; left: 0; width: 100%;
    display: flex; justify-content: center; align-items: center; gap: 20px;
  }
  .brand-dot {
    width: 44px; height: 44px; border-radius: 50%;
    background: var(--gold);
  }
  .brand-name {
    font-weight: 900; font-size: 62px; color: var(--ink);
    letter-spacing: 1px; line-height: 1;
  }
  .stripes { position: absolute; left: 0; top: 346px; width: 100%; height: 18px; }
  .stripe { position: absolute; left: 0; width: 100%; background: var(--band); }
  .stripe.one { top: 0; height: 4px; }
  .stripe.two { top: 7px; height: 4px; }
  .stripe.three { top: 14px; height: 4px; }
  .info-band {
    position: absolute; left: 0; top: 371px;
    width: 100%; height: 222px; background: var(--band);
  }
  .person {
    position: absolute; right: 548px; top: 48px; text-align: right;
  }
  .person-name { color: var(--gold); font-weight: 700; font-size: 20px; }
  .person-title { color: var(--white); font-size: 15px; margin-top: 8px; }
  .address {
    position: absolute; right: 548px; top: 140px;
    color: var(--white); font-weight: 700; font-size: 17px; white-space: nowrap;
  }
  .divider {
    position: absolute; left: 500px; top: 40px; width: 2px; height: 140px;
    background: linear-gradient(180deg, transparent, var(--rule) 30%, var(--rule) 70%, transparent);
  }
  .contacts { position: absolute; left: 538px; top: 42px; list-style: none; }
  .contact {
    display: flex; align-items: center; gap: 18px;
    color: var(--white); font-size: 17px; height: 40px;
  }
  .contact svg { width: 20px; height: 20px; fill: var(--gold); flex: none; }
</style>
</head>
<body>
  <main class="card">
    <div class="brand">
      <span class="brand-dot"></span>
      <span class="brand-name">Vireo Oil &amp; Gas</span>
    </div>

    <div class="stripes">
      <span class="stripe one"></span>
      <span class="stripe two"></span>
      <span class="stripe three"></span>
    </div>

    <section class="info-band">
      <div class="person">
        <p class="person-name">Dana Whitfield</p>
        <p class="person-title">Chief Executive Officer</p>
      </div>
      <p class="address">4410 Ridgeline Pkwy, Suite 210, NC 27500</p>

      <span class="divider"></span>

      <ul class="contacts">
        <li class="contact">
          <svg viewBox="0 0 20 20" aria-hidden="true"><path d="M2 7c0-2 2-4 8-4s8 2 8 4v2h-4V7.5c-1-.6-2.5-.9-4-.9s-3 .3-4 .9V9H2z"/><path d="M5 10h10l2 7H3z"/><circle cx="10" cy="13.5" r="1.8" fill="#0b0b0c"/></svg>
          <span>555.301.4478</span>
        </li>
        <li class="contact">
          <svg viewBox="0 0 20 20" aria-hidden="true"><rect x="5" y="2" width="10" height="5"/><rect x="1" y="8" width="18" height="7" rx="1"/><rect x="5" y="13" width="10" height="5"/><rect x="6.5" y="14.5" width="7" height="1.2" fill="#0b0b0c"/></svg>
          <span>555.301.4492</span>
        </li>
        <li class="contact">
          <svg viewBox="0 0 20 20" aria-hidden="true"><rect x="1" y="4" width="18" height="12"/><path d="M1.5 4.5 10 11l8.5-6.5" fill="none" stroke="#0b0b0c" stroke-width="1.5"/></svg>
          <span>dwhitfield@vireooilgas.example</span>
        </li>
      </ul>
    </section>
  </main>
</body>
</html>
```